Bref créative
Dravel & Partners
Global Medical Device Regulatory Affairs and Quality Specialist
Professional
Merrin T. Halvorsen
President
14 Quarry Mill Road
Cicero, IN 46108
merrinhalvorsen@dravelandpart.example
www.dravelandpart.example
Please visit our website at http://dravelandpart.example/default.php# to see colors needed to be used in design.
Logo and subtitle with web address(this information should also be on the front of the card.)

```html
<!DOCTYPE html>
<html lang="en">
<head>
<meta charset="utf-8">
<title>Dravel &amp; Partners — Business Card</title>
<link href="https://fonts.googleapis.com/css2?family=Cormorant+SC:wght@600&family=PT+Serif&family=Source+Sans+3:wght@400;700&display=swap" rel="stylesheet">
<style>
  :root {
    --backdrop: #d9d9d9;
    --card: #ffffff;
    --card-edge: #f1f1f3;
    --navy: #2b2e6f;
    --ink: #2a2a2a;
    --gold: #c29a2f;
    --rule: #9a9a9a;
    --icon: #3a3f7a;
  }
  * { margin: 0; padding: 0; box-sizing: border-box; }
  html, body {
    width: 1200px; height: 780px; overflow: hidden;
    background: var(--backdrop);
  }
  .canvas { position: relative; width: 1200px; height: 780px; }
  .card {
    position: absolute; left: 75px; top: 90px;
    width: 1050px; height: 600px;
    border-radius: 36px;
    background: linear-gradient(160deg, var(--card) 55%, var(--card-edge));
    box-shadow: 0 6px 18px rgba(0,0,0,.18);
    overflow: hidden;
  }
  .brand { position: absolute; left: 60px; top: 92px; display: flex; align-items: center; }
  .brand-dot {
    width: 140px; height: 140px; border-radius: 50%;
    background: var(--navy);
  }
  .brand-rule { width: 2px; height: 130px; background: var(--rule); margin: 0 22px 0 26px; }
  .brand-name {
    font-family: "Cormorant SC", serif; font-weight: 600;
    font-size: 64px; line-height: 1; color: var(--ink);
    letter-spacing: 1px;
  }
  .brand-tagline {
    font-family: "Cormorant SC", serif; font-weight: 600;
    font-size: 19px; color: var(--ink); letter-spacing: .6px;
    margin-top: 10px; white-space: nowrap;
  }
  .person { position: absolute; left: 690px; top: 322px; text-align: center; width: 320px; }
  .person-name {
    font-family: "Source Sans 3", sans-serif; font-weight: 700;
    font-size: 34px; color: var(--navy);
  }
  .person-title {
    font-family: "Source Sans 3", sans-serif; font-weight: 400;
    font-size: 22px; color: var(--gold); margin-top: 2px;
  }
  .contact {
    position: absolute; left: 72px; top: 390px;
    font-family: "PT Serif", serif; font-size: 23px; color: var(--ink);
    list-style: none;
  }
  .contact li { display: flex; align-items: center; height: 36px; }
  .contact .address { margin-bottom: 8px; }
  .contact svg { width: 20px; height: 20px; margin-right: 10px; fill: var(--icon); flex: none; }
  .phones span { display: flex; align-items: center; margin-right: 28px; }
</style>
</head>
<body>
<main class="canvas">
  <section class="card">
    <header class="brand">
      <div class="brand-dot"></div>
      <div class="brand-rule"></div>
      <div>
        <h1 class="brand-name">Dravel &amp; Partners</h1>
        <p class="brand-tagline">Global Medical Device Regulatory Affairs &amp; Quality Specialist</p>
      </div>
    </header>

    <div class="person">
      <p class="person-name">Merrin T. Halvorsen</p>
      <p class="person-title">President</p>
    </div>

    <ul class="contact">
      <li class="address">14 Quarry Mill Road Cicero, IN 46108</li>
      <li class="phones">
        <span><svg viewBox="0 0 24 24"><path d="M6.6 10.8a15 15 0 0 0 6.6 6.6l2.2-2.2a1 1 0 0 1 1-.25 11.4 11.4 0 0 0 3.6.57 1 1 0 0 1 1 1V20a1 1 0 0 1-1 1A17 17 0 0 1 3 4a1 1 0 0 1 1-1h3.5a1 1 0 0 1 1 1c0 1.25.2 2.45.57 3.57a1 1 0 0 1-.25 1z"/></svg>(317) 555-0142</span>
        <span><svg viewBox="0 0 24 24"><path d="M6 2h9l3 3v5H6z M4 11h16a2 2 0 0 1 2 2v7a2 2 0 0 1-2 2H4a2 2 0 0 1-2-2v-7a2 2 0 0 1 2-2z"/></svg>(317) 555-0187</span>
      </li>
      <li><svg viewBox="0 0 24 24"><path d="M12 2a10 10 0 1 0 5 18.7l-1-1.7A8 8 0 1 1 20 12v1a2 2 0 0 1-4 0V7h-2v1a5 5 0 1 0 .9 7 4 4 0 0 0 7.1-2v-1A10 10 0 0 0 12 2zm0 13a3 3 0 1 1 0-6 3 3 0 0 1 0 6z"/></svg>merrinhalvorsen@dravelandpart.example</li>
      <li><svg viewBox="0 0 24 24"><path d="M12 2a10 10 0 1 0 0 20 10 10 0 0 0 0-20zm6.9 6h-3a15 15 0 0 0-1.3-4A8 8 0 0 1 18.9 8zM12 4c.8 1.2 1.5 2.5 1.9 4h-3.8c.4-1.5 1.1-2.8 1.9-4zM4.3 14a8 8 0 0 1 0-4h3.4a16 16 0 0 0 0 4zm.8 2h3a15 15 0 0 0 1.3 4A8 8 0 0 1 5.1 16zm3-8h-3a8 8 0 0 1 4.3-4 15 15 0 0 0-1.3 4zM12 20c-.8-1.2-1.5-2.5-1.9-4h3.8c-.4 1.5-1.1 2.8-1.9 4zm2.3-6H9.7a14 14 0 0 1 0-4h4.6a14 14 0 0 1 0 4zm.3 6a15 15 0 0 0 1.3-4h3a8 8 0 0 1-4.3 4zm1.7-6a16 16 0 0 0 0-4h3.4a8 8 0 0 1 0 4z"/></svg>www.dravelandpart.example</li>
    </ul>
  </section>
</main>
</body>
</html>
```